Business card for a new cabinet shop company named Marlowe Cabinets for high end cabinets

Design a business card, thinking dark rich green with colours to speak of high end luxury ie; cream, gold, black possibly

Peter Lindqvar
Director Craftsman
Email: info@marlowecabinets.com.au
Instagram : @marlowe.cabinets

```html
<!DOCTYPE html>
<html lang="en">
<head>
<meta charset="utf-8">
<title>Marlowe Cabinets – Business Card</title>
<link rel="stylesheet" href="https://fonts.googleapis.com/css2?family=Jost:wght@400;500&display=swap">
<style>
  :root {
    --backdrop: #1b1b1c;
    --green: #0a4a30;
    --green-deep: #083f29;
    --black: #232323;
    --gold: #c9a964;
    --cream: #f4f1ea;
  }
  * { box-sizing: border-box; margin: 0; padding: 0; }
  html, body {
    width: 1200px; height: 801px; overflow: hidden;
    background: var(--backdrop);
    font-family: "Jost", sans-serif;
  }
  .stage {
    width: 1200px; height: 801px;
    display: flex; align-items: center; justify-content: center; gap: 40px;
  }
  .card {
    position: relative;
    width: 540px; height: 309px;
    overflow: hidden;
    box-shadow: 0 14px 30px rgba(0,0,0,.55);
  }

  /* Front */
  .card-front { background: var(--green); }
  .front-brand {
    position: absolute; left: 0; top: 0; width: 100%; height: 172px;
    display: flex; align-items: center; justify-content: center;
  }
  .wordmark {
    color: var(--gold);
    font-weight: 500;
    font-size: 38px;
    letter-spacing: .02em;
    white-space: nowrap;
  }
  .front-band {
    position: absolute; left: 0; bottom: 0; width: 100%; height: 137px;
    background: var(--black);
    border-top: 3px solid var(--gold);
    display: flex; align-items: center;
    padding: 0 34px;
  }
  .person { flex: 0 0 auto; }
  .person-name {
    color: var(--gold); font-weight: 500; font-size: 26px; line-height: 1.1;
  }
  .person-role {
    color: var(--cream); font-weight: 400; font-size: 14px;
    letter-spacing: .04em; margin-top: 4px;
  }
  .divider {
    width: 1px; height: 62px; background: var(--gold);
    margin: 0 24px; flex: 0 0 auto;
  }
  .contacts { list-style: none; display: flex; flex-direction: column; gap: 8px; }
  .contact {
    display: flex; align-items: center; gap: 9px;
    color: var(--cream); font-size: 12.5px; letter-spacing: .02em;
    white-space: nowrap;
  }
  .contact svg { width: 13px; height: 13px; flex: 0 0 auto; }

  /* Back */
  .card-back { background: var(--green-deep); }
  .back-field {
    position: absolute; inset: 0;
    background: linear-gradient(135deg, #0b4d32 0%, #08412a 100%);
  }
  .back-brand {
    position: absolute; inset: 0;
    display: flex; align-items: center; justify-content: center;
  }
  .back-brand .wordmark { font-size: 44px; }
</style>
</head>
<body>
<main class="stage">

  <section class="card card-front" aria-label="Business card front">
    <div class="front-brand">
      <span class="wordmark">Marlowe Cabinets</span>
    </div>
    <div class="front-band">
      <div class="person">
        <p class="person-name">Peter Lindqvar</p>
        <p class="person-role">Director Craftsman</p>
      </div>
      <span class="divider"></span>
      <ul class="contacts">
        <li class="contact">
          <svg viewBox="0 0 14 14" aria-hidden="true"><circle cx="7" cy="7" r="5.5" fill="none" stroke="#c9a964" stroke-width="1.6"/></svg>
          @marlowe.cabinets
        </li>
        <li class="contact">
          <svg viewBox="0 0 14 14" aria-hidden="true"><rect x="1" y="3" width="12" height="8" fill="#c9a964"/><path d="M1 3 L7 8 L13 3" fill="none" stroke="#232323" stroke-width="1.2"/></svg>
          info@marlowecabinets.com.au
        </li>
        <li class="contact">
          <svg viewBox="0 0 14 14" aria-hidden="true"><circle cx="7" cy="7" r="5.8" fill="none" stroke="#c9a964" stroke-width="1.3"/><ellipse cx="7" cy="7" rx="2.5" ry="5.8" fill="none" stroke="#c9a964" stroke-width="1.1"/><line x1="1.2" y1="7" x2="12.8" y2="7" stroke="#c9a964" stroke-width="1.1"/></svg>
          marlowecabinets.com.au
        </li>
      </ul>
    </div>
  </section>

  <section class="card card-back" aria-label="Business card back">
    <div class="back-field" role="img" aria-label="Faint repeating monogram pattern in darker green"></div>
    <div class="back-brand">
      <span class="wordmark">Marlowe Cabinets</span>
    </div>
  </section>

</main>
</body>
</html>
```